New Wix Website Design Project For New Finance Company

Create new design for a new page. Website should match existing theme of presentation deck, business card and logo attached to the brief. The site will have five pages

1) Home
2) Investment Criteria
3) Approach
4) Team
5) Contact

Some examples include
http://www.kestelvalefunds.com/

Although not a requirement, if the below white fence or similar could be added subtly to the sight as well, that would be great.

https://www.brovix.com/search?q=white+fence+horse&src=img&page=1#view=tr8KpL2wQz:

Target Market(s)

Business Professionals

Font styles to use
Sans Serif

Colors

Designer to choose colors to be used in the design.

Requirements
Must have
• Clean layout. Easy to upload header and footer.

```html
<!DOCTYPE html>
<html lang="en">
<head>
<meta charset="utf-8">
<title>Ashmere Ridge Capital</title>
<link href="https://fonts.googleapis.com/css2?family=Raleway:wght@400;600;700;800&family=Open+Sans:wght@400;600&display=swap" rel="stylesheet">
<style>
:root{
  --blue:#0868bf;
  --blue-dark:#04509a;
  --ink:#1c1c1c;
  --text:#7a7a7a;
  --grey-bg:#ececec;
  --card-dark:#2f2f2f;
  --footer:#070707;
  --white:#ffffff;
}
*{margin:0;padding:0;box-sizing:border-box}
html,body{width:1200px;height:3564px;overflow:hidden}
body{font-family:'Open Sans',Arial,sans-serif;color:var(--text);background:var(--white);position:relative}
.section{position:absolute;left:0;width:1200px}
.heading{font-family:'Raleway',Arial,sans-serif;font-weight:700;color:var(--blue);text-align:center;font-size:42px;letter-spacing:.5px}
.btn{position:absolute;display:flex;align-items:center;justify-content:center;background:var(--blue);color:var(--white);font-family:'Raleway',Arial,sans-serif;font-weight:600;font-size:18px;border-radius:26px}
p{font-size:14.5px;line-height:28px}

/* top bar */
.topbar{top:0;height:40px;background:var(--blue);color:var(--white);font-size:15px}
.topbar .item{position:absolute;top:0;height:40px;display:flex;align-items:center;gap:10px}

/* header */
.header{top:40px;height:96px;background:var(--white)}
.brand{position:absolute;left:76px;top:22px;text-align:center;white-space:nowrap}
.brand .name{font-family:'Raleway',Arial,sans-serif;font-weight:800;font-size:32px;color:var(--blue);line-height:34px;letter-spacing:1px}
.brand .sub{font-family:'Raleway',Arial,sans-serif;font-weight:800;font-size:13px;color:var(--blue);letter-spacing:6px;margin-top:2px}
.nav{position:absolute;right:70px;top:28px;display:flex;align-items:center}
.nav a{font-family:'Raleway',Arial,sans-serif;font-weight:600;font-size:15px;color:var(--ink);text-decoration:none;padding:11px 22px;border-radius:22px}
.nav a.active{background:var(--blue);color:var(--white)}

/* hero */
.hero{top:136px;height:541px;background:linear-gradient(90deg,#3b4656 0%,#6d7684 35%,#2d3848 70%,#1b2432 100%)}
.hero .photo{position:absolute;inset:0}
.hero h1{position:absolute;right:88px;top:160px;text-align:right;font-family:'Raleway',Arial,sans-serif;font-weight:800;font-size:62px;line-height:68px;color:var(--white);letter-spacing:1px;white-space:nowrap}
.hero .tag{position:absolute;right:88px;top:305px;color:var(--white);font-weight:600;font-size:16px}
.hero .arrow{position:absolute;top:380px;width:40px;height:40px}

/* welcome */
.welcome{top:677px;height:416px}
.welcome .heading{margin-top:60px}
.welcome .copy{width:700px;margin:16px auto 0;text-align:center}
.welcome .copy p{font-size:14px;line-height:28px;margin-bottom:12px}

/* approach */
.approach{top:1093px;height:430px;background:var(--grey-bg)}
.approach .heading{margin-top:60px}
.pillar{position:absolute;top:145px;width:320px}
.pillar .icon{width:84px;height:84px;background:var(--blue);display:flex;align-items:center;justify-content:center}
.pillar h3{font-family:'Raleway',Arial,sans-serif;font-weight:700;font-size:18px;color:var(--ink);margin-top:20px}
.pillar p{font-size:14px;line-height:26px;margin-top:8px}

/* criteria */
.criteria-band{top:1523px;height:210px;background:var(--blue)}
.criteria-band .heading{color:var(--white);margin-top:60px}
.criteria{top:1733px;height:655px;background:#f4f6f8}
.criteria .chart{position:absolute;left:78px;top:40px;width:600px;height:560px;background:linear-gradient(160deg,#e4ebf3 0%,#c9d9ea 100%)}
.criteria .side{position:absolute;left:758px;top:172px;width:360px}
.criteria .side h2{font-family:'Raleway',Arial,sans-serif;font-weight:700;font-size:32px;color:var(--blue)}
.criteria .side p{font-size:14px;line-height:28px;margin-top:10px}

/* team */
.team{top:2388px;height:496px}
.team .heading{margin-top:60px}
.member{position:absolute;top:142px;width:238px;height:290px}
.member .photo{height:220px;background:linear-gradient(180deg,#eceff2,#cfd4da)}
.member .bar{height:70px;background:var(--card-dark);color:var(--white);text-align:center;padding-top:14px}
.member .bar strong{display:block;font-family:'Raleway',Arial,sans-serif;font-weight:700;font-size:16px}
.member .bar span{font-size:13px;color:#bdbdbd}
.member.featured .photo{background:linear-gradient(180deg,#5b9bd5,#3a7fc2);position:relative;border:12px solid #e6eef6}
.member.featured .bar{background:var(--blue)}
.member.featured .bar span{color:var(--white)}
.member.featured .dots{position:absolute;left:50%;top:50%;transform:translate(-50%,-50%);display:flex;gap:12px}
.member.featured .dots i{width:34px;height:34px;border-radius:50%;border:2px solid var(--white);display:block}

/* cta */
.cta{top:2884px;height:328px;background:linear-gradient(180deg,#0b64b8 0%,#1a72c2 50%,#0a5aa8 100%)}
.cta h2{font-family:'Raleway',Arial,sans-serif;font-weight:700;color:var(--white);font-size:36px;line-height:48px;text-align:center;margin-top:84px}
.cta .btn{background:var(--white);color:var(--blue);left:508px;top:193px;width:183px;height:50px}

/* footer */
.footer{top:3212px;height:352px;background:var(--footer);color:#cfcfcf}
.footer .brand{left:76px;top:108px;width:238px}
.footer .brand .name{font-size:24px;line-height:28px}
.footer .brand .sub{font-size:11px;letter-spacing:5px}
.footer .social{position:absolute;left:134px;top:172px;display:flex;gap:8px}
.footer .social i{width:38px;height:38px;border-radius:50%;display:block;background:var(--blue)}
.fcol{position:absolute;top:38px;width:240px}
.fcol h4{font-family:'Raleway',Arial,sans-serif;font-weight:700;font-size:18px;color:var(--blue);letter-spacing:.5px}
.fcol ul{list-style:none;margin-top:20px}
.fcol li{font-size:13.5px;line-height:31px;padding-left:18px;position:relative}
.fcol li::before{content:"";position:absolute;left:0;top:13px;width:6px;height:6px;border-radius:50%;background:var(--blue)}
.contact-row{display:flex;gap:14px;font-size:13.5px;line-height:22px;margin-top:12px}
.contact-row svg{flex:none;margin-top:2px}
.fcol p{font-size:13.5px;line-height:26px;margin-top:14px}
.fcol .email{margin-top:12px;height:40px;width:240px;background:var(--white);color:#888;font-size:13px;display:flex;align-items:center;padding-left:12px}
.fcol .btn{position:static;width:164px;height:40px;margin-top:10px;font-size:17px;font-weight:700}
.footer .rule{position:absolute;left:76px;right:76px;top:288px;height:1px;background:#2a2a2a}
.footer .copy{position:absolute;left:0;right:0;top:312px;text-align:center;font-size:13px}
</style>
</head>
<body>

<div class="section topbar">
  <div class="item" style="left:780px">
    <svg width="18" height="18" viewBox="0 0 24 24"><path fill="#fff" d="M6.6 10.8a15.1 15.1 0 0 0 6.6 6.6l2.2-2.2c.3-.3.7-.4 1-.2 1.1.4 2.3.6 3.6.6.6 0 1 .4 1 1V20c0 .6-.4 1-1 1A17 17 0 0 1 3 4c0-.6.4-1 1-1h3.5c.6 0 1 .4 1 1 0 1.3.2 2.5.6 3.6.1.3 0 .7-.2 1z"/></svg>
    <span>123 456 7890</span>
  </div>
  <div class="item" style="left:940px">
    <svg width="20" height="16" viewBox="0 0 20 16"><rect width="20" height="16" rx="2" fill="#fff"/><path d="M1 2l9 7 9-7" stroke="#0868bf" stroke-width="1.8" fill="none"/></svg>
    <span>info@AshmereRidge.com</span>
  </div>
</div>

<header class="section header">
  <div class="brand">
    <div class="name">ASHMERE RIDGE</div>
    <div class="sub">CAPITAL</div>
  </div>
  <nav class="nav">
    <a class="active">HOME</a>
    <a>INVESTMENT CRITERIA</a>
    <a>APPROACH</a>
    <a>TEAM</a>
    <a>CONTACT</a>
  </nav>
</header>

<section class="section hero">
  <div class="photo" role="img" aria-label="Smiling business professionals in suits seated at a meeting table"></div>
  <svg class="arrow" style="left:22px" viewBox="0 0 40 40"><circle cx="20" cy="20" r="20" fill="rgba(0,0,0,.35)"/><path d="M23 12l-8 8 8 8" stroke="#fff" stroke-width="2" fill="none"/></svg>
  <svg class="arrow" style="right:22px" viewBox="0 0 40 40"><circle cx="20" cy="20" r="20" fill="rgba(0,0,0,.35)"/><path d="M17 12l8 8-8 8" stroke="#fff" stroke-width="2" fill="none"/></svg>
  <h1>ASHMERE RIDGE<br>CAPITAL</h1>
  <div class="tag">Lorem Ipsum is simply dummy text of the printing and type</div>
  <div class="btn" style="left:927px;top:361px;width:183px;height:52px">CONTACT US</div>
</section>

<section class="section welcome">
  <h2 class="heading">WELCOME TO ASHMERE RIDGE</h2>
  <div class="copy">
    <p>Lorem Ipsum is simply dummy text of the printing and typesetting industry. Lorem Ipsum has been the industry's standard dummy text ever since the printer took a galley.</p>
    <p>Lorem Ipsum is simply dummy text of the printing and typesetting industry. Lorem Ipsum has been the industry's standard dummy text ever since the 1500s, when an unknown printer took a galley of type and scrambled it to make a type specimen book. It has survived not only five centuries.</p>
  </div>
  <div class="btn" style="left:508px;top:302px;width:183px;height:50px">LEARN MORE</div>
</section>

<section class="section approach">
  <h2 class="heading">OUR APPROACH</h2>
  <div class="pillar" style="left:78px">
    <div class="icon"><svg width="56" height="36" viewBox="0 0 56 36"><path d="M2 18C10 6 19 2 28 2s18 4 26 16c-8 12-17 16-26 16S10 30 2 18z" fill="#fff"/><circle cx="28" cy="18" r="10" fill="#0868bf"/><circle cx="28" cy="18" r="5" fill="#fff"/></svg></div>
    <h3>VISION</h3>
    <p>Lorem Ipsum is simply dummy text of the printing and typesetting industry Ipsum has been the industry's</p>
  </div>
  <div class="pillar" style="left:444px">
    <div class="icon"><svg width="52" height="44" viewBox="0 0 52 44"><path d="M12 2h28l10 12-24 28L2 14z" fill="#fff"/><path d="M2 14h48M12 2l6 12 8 28 8-28 6-12M18 14l8-12 8 12" stroke="#0868bf" stroke-width="2" fill="none"/></svg></div>
    <h3>CORE VALUES</h3>
    <p>Lorem Ipsum is simply dummy text of the printing and typesetting industry Ipsum has been the industry's</p>
  </div>
  <div class="pillar" style="left:810px">
    <div class="icon"><svg width="52" height="52" viewBox="0 0 52 52"><circle cx="24" cy="28" r="21" fill="#fff"/><circle cx="24" cy="28" r="15" fill="#0868bf"/><circle cx="24" cy="28" r="10" fill="#fff"/><circle cx="24" cy="28" r="5" fill="#0868bf"/><path d="M24 28L46 6" stroke="#fff" stroke-width="3"/><path d="M40 4l8-2-2 8z" fill="#fff"/></svg></div>
    <h3>MISSION</h3>
    <p>Lorem Ipsum is simply dummy text of the printing and typesetting industry Ipsum has been the industry's</p>
  </div>
</section>

<section class="section criteria-band">
  <h2 class="heading">INVESTMENT CRITERIA</h2>
</section>

<section class="section criteria">
  <div class="chart" role="img" aria-label="Growth chart illustration showing rising investment returns"></div>
  <div class="side">
    <h2>ASHMERE RIDGE</h2>
    <p>Lorem Ipsum is simply dummy text of the printing and typesetting industry. Lorem Ipsum has been the industry's standard dummy text ever since the 1500s, when an unknown printer took a galley of type and scrambled it to make a type specimen book. It has survived not only five centuries.</p>
  </div>
  <div class="btn" style="left:758px;top:408px;width:183px;height:50px">LEARN MORE</div>
</section>

<section class="section team">
  <h2 class="heading">OUR TEAM</h2>
  <div class="member" style="left:78px">
    <div class="photo" role="img" aria-label="Portrait of a team member in a dark t-shirt"></div>
    <div class="bar"><strong>MEMBER NAME</strong><span>something.com</span></div>
  </div>
  <div class="member" style="left:347px">
    <div class="photo" role="img" aria-label="Portrait of a team member in a dark blazer"></div>
    <div class="bar"><strong>MEMBER NAME</strong><span>something.com</span></div>
  </div>
  <div class="member featured" style="left:615px">
    <div class="photo" role="img" aria-label="Portrait of a team member with a blue hover overlay"><div class="dots"><i></i><i></i></div></div>
    <div class="bar"><strong>MEMBER NAME</strong><span>something.com</span></div>
  </div>
  <div class="member" style="left:884px">
    <div class="photo" role="img" aria-label="Portrait of a team member in a dark blazer"></div>
    <div class="bar"><strong>MEMBER NAME</strong><span>something.com</span></div>
  </div>
</section>

<section class="section cta" role="img" aria-label="Blue-tinted background of people at a conference table">
  <h2>If You Need an Have any Question for<br>Contact Us Today !</h2>
  <div class="btn">CONTACT US</div>
</section>

<footer class="section footer">
  <div class="brand">
    <div class="name">ASHMERE RIDGE</div>
    <div class="sub">CAPITAL</div>
  </div>
  <div class="social">
    <i></i><i></i><i></i>
  </div>
  <div class="fcol" style="left:347px">
    <h4>SITEMAP</h4>
    <ul><li>Home</li><li>Investment Criteria</li><li>Approach</li><li>Team</li><li>Contact</li></ul>
  </div>
  <div class="fcol" style="left:615px">
    <h4>CONTACT US</h4>
    <div class="contact-row" style="margin-top:20px">
      <svg width="16" height="22" viewBox="0 0 16 22"><path d="M8 0a8 8 0 0 1 8 8c0 6-8 14-8 14S0 14 0 8a8 8 0 0 1 8-8z" fill="#0868bf"/><circle cx="8" cy="8" r="3" fill="#070707"/></svg>
      <div>ASHMERE RIDGE<br>101 - Lorem Ipsum simple text of print and type text.</div>
    </div>
    <div class="contact-row" style="margin-top:18px">
      <svg width="16" height="16" viewBox="0 0 24 24"><path fill="#0868bf" d="M6.6 10.8a15.1 15.1 0 0 0 6.6 6.6l2.2-2.2c.3-.3.7-.4 1-.2 1.1.4 2.3.6 3.6.6.6 0 1 .4 1 1V20c0 .6-.4 1-1 1A17 17 0 0 1 3 4c0-.6.4-1 1-1h3.5c.6 0 1 .4 1 1 0 1.3.2 2.5.6 3.6.1.3 0 .7-.2 1z"/></svg>
      <div>123 456 7890</div>
    </div>
    <div class="contact-row" style="margin-top:18px">
      <svg width="18" height="14" viewBox="0 0 20 16"><rect width="20" height="16" rx="2" fill="#0868bf"/><path d="M1 2l9 7 9-7" stroke="#070707" stroke-width="1.8" fill="none"/></svg>
      <div>hello@AshmereRidge.com</div>
    </div>
  </div>
  <div class="fcol" style="left:884px">
    <h4>NEWSLETTER</h4>
    <p>Would you like to receive our exclusive news and update for sign up our newsletter !</p>
    <div class="email">Enter Email *</div>
    <div class="btn">SUBSCRIBE</div>
  </div>
  <div class="rule"></div>
  <div class="copy">©CORLISS INVESTMENT GROUP - 2019 All Rights Reserved.</div>
</footer>

</body>
</html>
```